Court Horizon Trust Web site

We need a Wordpress web site for a new non-profit, the Court Horizon Trust. CHT's mission is to raise the awareness of sustainability within the tennis community and industry worldwide. Our focus is on education and being a catalyst in connecting expertise in the environmental field with tennis organizations to create sustainable change. Our primary targets are youth education and empowerment, tennis facility management, and Celebrity tennis players' engagement.

The design needs to be elegant and attractive to potential corporate donors and reflect the high level of sophistication of the tennis demographic. It needs to be very graphic with high-impact photos and the ability to inspire action. Although it can be simple now it will need to have the capability of expanding to allow acceptance of donations online, offering of information products in exchange for email registration, and potentially a membership-oriented section of the site with forums and community engagement.

At the present time, it is more of an information-oriented site that tells a compelling story and inspires people to take action to get involved in the way that most fits their needs.

We need to have the ability to add pages and blog posts easily on our own while maintaining a relationship that would allow us a cost-effective way of making more major additions and adjustments to the site.

Attached is our logo. Thanks for your desire to help us make an impact on the world.

Industry/Entity Type

Graphic Design

```html
<!DOCTYPE html>
<html lang="en">
<head>
<meta charset="utf-8">
<title>Court Horizon Trust</title>
<link href="https://fonts.googleapis.com/css2?family=Open+Sans:wght@300;400;600;700&display=swap" rel="stylesheet">
<style>
:root{
  --blue:#1b6a8c;
  --lime:#d3c800;
  --page:#f2f2f2;
  --hero-a:#c9c57a;
  --hero-b:#8d8a45;
  --text:#555;
  --footer:#3b4047;
  --footer-text:#a9aeb4;
  --white:#fff;
}
*{box-sizing:border-box;margin:0;padding:0}
html,body{width:875px;height:1200px;overflow:hidden}
body{position:relative;background:var(--page);font-family:"Open Sans",Arial,sans-serif;color:var(--text)}
.abs{position:absolute}
.hero{left:0;top:0;width:875px;height:320px;background:radial-gradient(ellipse at 25% 40%,var(--hero-a),var(--hero-b) 75%)}
.brand{left:170px;top:32px;display:flex;align-items:center;gap:6px;color:var(--blue);font-size:11px;font-weight:600;letter-spacing:.3px}
.brand-dot{width:12px;height:12px;border-radius:50%;background:var(--blue)}
.join{left:614px;top:55px;color:var(--white);font-size:8.5px;font-weight:600;display:flex;align-items:center;gap:5px}
.join i{width:8px;height:9px;background:var(--blue);display:block}
.nav{left:172px;top:79px;width:533px;height:37px;display:flex;background:var(--white)}
.nav a{flex:1;display:flex;align-items:center;justify-content:center;font-size:8.5px;color:#333;text-decoration:none;border-left:1px solid #e3e3e3}
.nav a.active{background:var(--blue);color:var(--white);font-weight:600;border:none}
.hero-title{left:0;width:875px;top:170px;text-align:center;color:var(--white);font-size:27px;font-weight:300;letter-spacing:.5px}
.hero-btn{left:405px;top:227px;width:86px;height:32px;border:2px solid var(--white);color:var(--blue);font-size:10px;font-weight:600;display:flex;align-items:center;justify-content:center}
.dots{left:428px;top:290px;display:flex;gap:4px}
.dots i{width:10px;height:10px;border-radius:50%;background:var(--lime);display:block}
.dots i:first-child{background:var(--blue)}
.card{top:355px;width:123px;height:178px}
.card .photo{height:137px}
.card .label{height:41px;background:var(--blue);color:var(--white);font-size:8.5px;font-weight:600;display:flex;align-items:center;justify-content:center}
.card.hover .label{background:var(--lime);color:#555;font-weight:400}
.welcome-photo{left:171px;top:576px;width:200px;height:140px;background:linear-gradient(135deg,#e8e8e8,#9a9a9a)}
.welcome{left:385px;top:568px;width:183px}
.welcome h1{color:var(--blue);font-size:34px;font-weight:400;line-height:1}
.welcome h2{font-size:13px;font-weight:400;color:#444;margin-top:2px}
.welcome p{font-size:7.6px;line-height:12px;margin-top:4px;text-align:justify}
.read-more{left:510px;top:697px;width:58px;height:18px;border:1px solid #444;font-size:6.5px;font-weight:600;color:#333;display:flex;align-items:center;justify-content:center}
.news{left:581px;top:571px}
.news h3{color:var(--blue);font-size:16px;font-weight:400}
.news ul{list-style:none;margin-top:9px}
.news li{font-size:7px;color:var(--blue);margin-bottom:6px;display:flex;gap:6px}
.news li::before{content:"›";color:var(--lime);font-weight:700}
.events-title{left:170px;top:757px;color:var(--blue);font-size:16px;font-weight:400}
.arrows{left:678px;top:757px}
.event{top:788px;width:123px}
.event .photo{height:65px;border-bottom:2px solid var(--blue)}
.date{position:absolute;top:73px;left:0;width:35px;height:37px;border:2px solid #bdbdbd;border-radius:3px;background:var(--white);text-align:center;color:var(--blue)}
.date b{display:block;font-size:11px;font-weight:600;margin-top:7px;line-height:1}
.date small{font-size:4.5px;font-weight:700}
.event-text{position:absolute;top:72px;left:42px;width:82px}
.event-text h4{color:var(--lime);font-size:7px;font-weight:400}
.event-text h5{color:#333;font-size:8px;font-weight:400}
.event-text p{font-size:5.4px;line-height:7px}
.banner{left:172px;top:946px;width:533px;height:129px;background:linear-gradient(120deg,#8a5535,#6d4029)}
.banner-text{left:248px;top:978px;color:var(--white);display:flex;align-items:flex-end;gap:8px}
.banner-text .words{font-size:24px;line-height:25px}
.banner-text .words b{font-weight:700;display:block}
.banner-text .words span{font-weight:300}
.banner-text .year{font-size:62px;font-weight:300;line-height:52px}
.banner-icon{left:588px;top:985px}
.footer{left:0;top:1121px;width:875px;height:79px;background:var(--footer)}
.f-col{top:1146px;font-size:7px;line-height:9px;color:var(--footer-text);display:flex;gap:14px}
.f-col svg{flex:none}
.legal{left:538px;top:1146px;font-size:7px;color:var(--footer-text)}
.legal b{color:var(--lime);font-weight:400}
.social{left:540px;top:1162px;display:flex;gap:4px}
.social i{width:16px;height:16px;border-radius:50%;background:#7f858c;display:block}
</style>
</head>
<body>
<div class="abs hero" role="img" aria-label="Close-up photo of a tennis ball behind court netting, tinted olive"></div>
<div class="abs brand"><span class="brand-dot"></span>COURT HORIZON TRUST</div>
<div class="abs join"><i></i>BECOME A MEMBER</div>
<nav class="abs nav">
  <a class="active">HOME</a><a>EVENTS</a><a>MEMBERS</a><a>BLOG</a><a>CONTACT</a>
</nav>
<div class="abs hero-title">BUILDING PROFESSIONAL TENNIS PLAYERS</div>
<div class="abs hero-btn">MORE INFO</div>
<div class="abs dots"><i></i><i></i><i></i></div>

<div class="abs card" style="left:171px"><div class="photo" role="img" aria-label="Young boy holding a tennis racket and ball" style="background:linear-gradient(#6aa86a,#2f7f3c)"></div><div class="label">JUNIOR TENNIS</div></div>
<div class="abs card hover" style="left:307px"><div class="photo" role="img" aria-label="Children training on a blue hard court" style="background:linear-gradient(#4e7fa0,#2d5f74)"></div><div class="label">LEARNING CENTER</div></div>
<div class="abs card" style="left:445px"><div class="photo" role="img" aria-label="Group of players resting courtside" style="background:linear-gradient(#9fb6bc,#6f8f86)"></div><div class="label">COMMUNITY</div></div>
<div class="abs card" style="left:582px"><div class="photo" role="img" aria-label="Adult player ready to return on court" style="background:linear-gradient(#8fa0a8,#4f6d7a)"></div><div class="label">ADULT TENNIS</div></div>

<div class="abs welcome-photo" role="img" aria-label="Black and white photo of a woman serving, wearing a yellow top"></div>
<div class="abs welcome">
  <h1>WELCOME</h1>
  <h2>TO OUR CLUB SITE</h2>
  <p>Lorem Ipsum is simply dummy text of the printing and typesetting industry. Lorem Ipsum has been the industry's standard dummy text ever since the 1500s, when an unknown printer took a galley of type and scrambled it to make a type specimen book. It has survived not only five centuries.</p>
</div>
<div class="abs read-more">READ MORE</div>
<div class="abs news">
  <h3>LATEST NEWS</h3>
  <ul><li>LOREM IPSUM DOLOR</li><li>LOREM IPSUM DOLOR</li><li>LOREM IPSUM DOLOR</li><li>LOREM IPSUM DOLOR</li><li>LOREM IPSUM DOLOR</li></ul>
</div>

<div class="abs events-title">UPCOMING EVENTS</div>
<svg class="abs arrows" width="26" height="16" viewBox="0 0 26 16"><path d="M9 2 3 8l6 6M17 2l6 6-6 6" fill="none" stroke="#d3c800" stroke-width="2.5"/></svg>

<div class="abs event" style="left:171px"><div class="photo" role="img" aria-label="Tennis balls and racket on green court" style="background:linear-gradient(#3f8a68,#1f5f4a)"></div>
  <div class="date"><b>14</b><small>MARCH</small></div>
  <div class="event-text"><h4>EVENT TITLE</h4><h5>Lorem Ipsum</h5><p>Lorem Ipsum is simply dummy text of the printing and typesetting industry.</p></div></div>
<div class="abs event" style="left:307px"><div class="photo" role="img" aria-label="Racket and balls on dark court" style="background:linear-gradient(#4d5a55,#2c3532)"></div>
  <div class="date"><b>18</b><small>JULY</small></div>
  <div class="event-text"><h4>EVENT TITLE</h4><h5>Lorem Ipsum</h5><p>Lorem Ipsum is simply dummy text of the printing and typesetting industry.</p></div></div>
<div class="abs event" style="left:445px"><div class="photo" role="img" aria-label="Player lunging for a forehand" style="background:linear-gradient(#6d8f5e,#2e4a2c)"></div>
  <div class="date"><b>24</b><small>AUGUST</small></div>
  <div class="event-text"><h4>EVENT TITLE</h4><h5>Lorem Ipsum</h5><p>Lorem Ipsum is simply dummy text of the printing and typesetting industry.</p></div></div>
<div class="abs event" style="left:582px"><div class="photo" role="img" aria-label="Two players at the net on a hard court" style="background:linear-gradient(#a5b9c6,#5f84a0)"></div>
  <div class="date"><b>30</b><small>SEPTEMBER</small></div>
  <div class="event-text"><h4>EVENT TITLE</h4><h5>Lorem Ipsum</h5><p>Lorem Ipsum is simply dummy text of the printing and typesetting industry.</p></div></div>

<div class="abs banner" role="img" aria-label="Tennis ball on a clay court line"></div>
<div class="abs banner-text"><div class="words"><b>TENNIS</b><span>TOURNAMENT</span></div><div class="year">2014</div></div>
<svg class="abs banner-icon" width="46" height="46" viewBox="0 0 46 46"><path d="M16 4h26v38H16" fill="none" stroke="#d3c800" stroke-width="4"/><path d="M4 23h22M18 14l9 9-9 9" fill="none" stroke="#d3c800" stroke-width="4"/></svg>

<div class="abs footer"></div>
<div class="abs f-col" style="left:172px"><svg width="10" height="14" viewBox="0 0 10 14"><path d="M5 0a5 5 0 0 0-5 5c0 4 5 9 5 9s5-5 5-9a5 5 0 0 0-5-5z" fill="#d3c800"/><circle cx="5" cy="5" r="2" fill="#3b4047"/></svg><div>COURT HORIZON TRUST<br>STREET NAME<br>CITY NAME</div></div>
<div class="abs f-col" style="left:341px"><svg width="9" height="14" viewBox="0 0 9 14"><rect x="0.8" y="0.8" width="7.4" height="12.4" rx="1" fill="none" stroke="#d3c800" stroke-width="1.6"/></svg><div>TELEPHONE: +1 800 555 4444<br>E-MAIL:<br>MAIL@YOURMAIL.COM</div></div>
<div class="abs legal"><b>COURT HORIZON TRUST</b> © 2014 | Privacy Policy</div>
<div class="abs social"><i></i><i></i><i></i><i></i></div>
</body>
</html>
```